Boom Way Hoist Service Business Cards

I need a business card for "Boom Way Hoist and Haulage"

Boomway2023@hoistmail.net

Hoist Works LLC, Boom Way Hoist and Haulage LLC

555.014.7260 | www.BOOMWAYHOISTS.example

Central Indiana & Northeast Ohio

(IN) 14820 Maple Lane Noblesville, IN 46000

(OH) 2450 Pell Street Akron, Ohio 44300

Colors
0094D4
00A9DD
6FCCEA
C7EBF8
E9F6FB
59FF00
82FF00
B8FF75
E3FFCB
F4FFEA
EE7325
F08F49
F5BC92
FAE3D3
FDF4ED
EB3D1F
EC4F4E
F09395
F8D3D4
FCEDEE
E54698
E96AAD
F1A4CE
F9D9EA
FCEFF6
A7469A
B969AE
D3A5CF
EDDBEB
F8F0F9

```html
<!DOCTYPE html>
<html lang="en">
<head>
<meta charset="utf-8">
<title>Boom Way Hoist Service Business Cards</title>
<link rel="stylesheet" href="https://fonts.googleapis.com/css2?family=Poppins:wght@400;500;700;800&display=swap">
<style>
  :root {
    --green: #46b64a;
    --red: #eb3d1f;
    --ink: #1d1d1d;
    --paper: #ffffff;
    --backdrop: #e6e8e6;
    --crane-grey: #9a9a9a;
  }
  * { box-sizing: border-box; margin: 0; padding: 0; }
  html, body { width: 1200px; height: 864px; overflow: hidden; }
  body {
    background: var(--backdrop);
    font-family: "Poppins", sans-serif;
    color: var(--ink);
    position: relative;
  }
  .card {
    position: absolute;
    width: 595px;
    height: 340px;
    border-radius: 26px;
    overflow: hidden;
    box-shadow: 0 6px 18px rgba(0,0,0,0.12);
  }
  .card-front {
    left: 70px;
    top: 60px;
    background: var(--green);
    display: flex;
    align-items: center;
    justify-content: center;
  }
  .brand-name {
    color: var(--paper);
    font-weight: 800;
    font-size: 46px;
    line-height: 1.05;
    text-align: center;
    text-transform: uppercase;
    letter-spacing: 1px;
  }
  .brand-name .sub {
    display: block;
    font-size: 20px;
    letter-spacing: 2px;
    margin-top: 8px;
  }
  .card-back {
    left: 535px;
    top: 464px;
    background: var(--paper);
  }
  .swoosh { position: absolute; inset: 0; width: 100%; height: 100%; }
  .addresses {
    position: absolute;
    right: 34px;
    top: 28px;
    text-align: right;
    font-size: 15px;
    line-height: 1.45;
    font-style: normal;
    font-weight: 400;
  }
  .entities {
    position: absolute;
    right: 34px;
    top: 124px;
    text-align: right;
    font-size: 15px;
    line-height: 1.45;
  }
  .crane-art {
    position: absolute;
    left: 46px;
    top: 66px;
    width: 140px;
    height: 140px;
    border-radius: 6px;
    background: linear-gradient(135deg, #d9d9d9 0%, var(--crane-grey) 45%, #4caf50 75%, #e0503a 100%);
  }
  .contacts {
    position: absolute;
    left: 46px;
    top: 214px;
    list-style: none;
    font-size: 15px;
    line-height: 1.55;
  }
  .contacts li { display: flex; align-items: center; gap: 8px; }
  .contacts svg { width: 14px; height: 14px; flex: none; }
</style>
</head>
<body>
  <section class="card card-front">
    <h1 class="brand-name">Boom Way<span class="sub">Hoist Service</span></h1>
  </section>

  <section class="card card-back">
    <svg class="swoosh" viewBox="0 0 595 340" aria-hidden="true">
      <path d="M0 340 L0 332 L300 322 Q420 318 470 240 Q500 198 540 196 L595 192 L595 340 Z" fill="var(--green)"/>
      <path d="M0 314 L280 302 Q370 298 440 214 L456 214 Q385 308 285 311 L0 323 Z" fill="var(--red)"/>
    </svg>

    <address class="addresses">
      Central Indiana &amp; Northeast Ohio<br>
      (IN) 14820 Maple Lane Noblesville, IN 46000<br>
      (OH) 2450 Pell Street Akron, Ohio 44300
    </address>

    <p class="entities">Hoist Works LLC,<br>Boom Way Hoist and Haulage LLC</p>

    <div class="crane-art" role="img" aria-label="Illustration of a mobile crane truck lifting a load in front of city buildings"></div>

    <ul class="contacts">
      <li>
        <svg viewBox="0 0 16 16"><path d="M3 2 L6 2 L7 5 L5 6.5 C6 8.5 7.5 10 9.5 11 L11 9 L14 10 L14 13 C14 14 13 14.5 12 14.5 C6.5 14 2 9.5 1.5 4 C1.5 3 2 2 3 2 Z" fill="var(--green)"/></svg>
        555.014.7260
      </li>
      <li>
        <svg viewBox="0 0 16 16"><rect x="1" y="3" width="14" height="10" rx="1.5" fill="var(--green)"/><path d="M1.5 4 L8 9 L14.5 4" stroke="#fff" stroke-width="1.4" fill="none"/></svg>
        Boomway2023@hoistmail.net
      </li>
      <li>
        <svg viewBox="0 0 16 16"><circle cx="8" cy="8" r="7" fill="var(--green)"/><path d="M1 8 H15 M8 1 C5 4 5 12 8 15 M8 1 C11 4 11 12 8 15" stroke="#fff" stroke-width="1" fill="none"/></svg>
        www.BOOMWAYHOISTS.example
      </li>
    </ul>
  </section>
</body>
</html>
```